Business Card Design Project

Velvet Harbor is a Boutique Clothing. On the business cards I would like to have this included
Website: www.velvetharbor-example.com
Email: shop@velvetharbor-example.com
Owner: Mai Torres & Bo Rinaldi

Industry/Entity Type

Business

Contact Information for Business Card

I wanted something simple and elegant. I have attach business logo.

```html
<!DOCTYPE html>
<html lang="en">
<head>
<meta charset="utf-8">
<title>Velvet Harbor – Business Card</title>
<link href="https://fonts.googleapis.com/css2?family=Lato:ital,wght@0,300;0,400;1,700&display=swap" rel="stylesheet">
<style>
  :root {
    --backdrop: #e9e7e3;
    --card-white: #ffffff;
    --card-mist: #f4f5f7;
    --ink: #1f1f1f;
    --panel-dark: #2b2b2b;
    --panel-shade: #3b3b3b;
    --text-light: #ffffff;
  }
  html, body {
    margin: 0;
    padding: 0;
    width: 1200px;
    height: 800px;
    overflow: hidden;
    background: var(--backdrop);
    font-family: "Lato", sans-serif;
  }
  .canvas {
    position: relative;
    width: 1200px;
    height: 800px;
  }
  .card {
    position: absolute;
    top: 251px;
    width: 520px;
    height: 297px;
    box-shadow: 0 8px 24px rgba(0,0,0,0.12);
    overflow: hidden;
  }
  .card--logo-side { left: 60px; background: var(--card-white); }
  .card--contact-side { left: 620px; background: var(--card-mist); }
  .card__panel {
    position: absolute;
    inset: 0;
    width: 100%;
    height: 100%;
  }
  .panel-dark { fill: var(--panel-dark); }
  .panel-shade { fill: var(--panel-shade); }
  .contact {
    position: absolute;
    left: 44px;
    top: 142px;
    color: var(--text-light);
  }
  .contact__names {
    margin: 0;
    font-size: 18px;
    font-weight: 700;
    font-style: italic;
    letter-spacing: 0.2px;
  }
  .contact__role {
    margin: 0 0 22px;
    font-size: 16px;
    font-weight: 300;
  }
  .contact__line {
    margin: 0;
    font-size: 15px;
    font-weight: 400;
    line-height: 21px;
  }
  .brand {
    position: absolute;
    display: flex;
    align-items: center;
    justify-content: center;
    border: 1.5px solid var(--ink);
    border-radius: 50%;
    color: var(--ink);
    font-weight: 400;
    text-align: center;
    letter-spacing: 2px;
    text-transform: uppercase;
  }
  .card--logo-side .brand {
    width: 170px;
    height: 170px;
    left: 175px;
    top: 63px;
    font-size: 17px;
  }
  .card--contact-side .brand {
    width: 130px;
    height: 130px;
    left: 366px;
    top: 84px;
    font-size: 13px;
  }
</style>
</head>
<body>
<main class="canvas">
  <section class="card card--logo-side">
    <div class="brand">Velvet<br>Harbor</div>
  </section>

  <section class="card card--contact-side">
    <svg class="card__panel" viewBox="0 0 520 297" preserveAspectRatio="none" aria-hidden="true">
      <polygon class="panel-dark" points="0,0 229,0 364,297 0,297"/>
      <polygon class="panel-shade" points="0,0 229,0 0,119"/>
    </svg>
    <div class="contact">
      <p class="contact__names">Mai Torres &amp; Bo Rinaldi</p>
      <p class="contact__role">owner</p>
      <p class="contact__line">www.velvetharbor-example.com</p>
      <p class="contact__line">shop@velvetharbor-example.com</p>
    </div>
    <div class="brand">Velvet<br>Harbor</div>
  </section>
</main>
</body>
</html>
```